RESIDENCE VALBRUNE

The CORVALE Immobilier company exclusively offers apartments for sale under a tax exemption law (BELTRAVIGNE) in CAMBRAI, 92 apartments are available, fully renovated with balcony, terrace, elevator, in a former military residence known to the city.
We want to make a book to give to our customers.

```html
<!DOCTYPE html>
<html lang="fr">
<head>
<meta charset="utf-8">
<title>Loi Beltravigne — Résidence Valbrune</title>
<link href="https://fonts.googleapis.com/css2?family=Crimson+Text:wght@400;600&display=swap" rel="stylesheet">
<style>
  :root {
    --backdrop: #000000;
    --paper: #ffffff;
    --ink: #111111;
    --fold: #555555;
    --cell-head: #85c99a;
    --cell-row: #a8d8b4;
    --cell-accent: #b2d56a;
  }
  * { margin: 0; padding: 0; box-sizing: border-box; }
  html, body { width: 1200px; height: 675px; overflow: hidden; background: var(--backdrop); }
  body { position: relative; font-family: "Crimson Text", Georgia, serif; color: var(--ink); }

  .spread { position: absolute; left: 7.5px; top: 128px; width: 1184.5px; height: 418px; background: var(--paper); }
  .page { position: absolute; top: 0; height: 100%; }
  .page--left { left: 0; width: 592.5px; }
  .page--right { left: 592.5px; width: 592px; border-left: 1px solid var(--fold); }

  .page-title { position: absolute; font-weight: 400; font-size: 22px; line-height: 1; letter-spacing: -0.1px; white-space: nowrap; }
  .page--left .page-title { left: 57.5px; top: 68px; }
  .page--right .page-title { left: 37.5px; top: 128px; }

  .body-text { position: absolute; font-size: 8px; line-height: 10.1px; }
  .intro { left: 57.5px; top: 166px; width: 200px; }
  .note { left: 259.5px; top: 353px; width: 300px; }
  .principle { left: 37.5px; top: 159px; width: 266.5px; text-align: justify; }
  .principle p + p { margin-top: 10.5px; }

  .rent-table { position: absolute; left: 283.5px; top: 149.5px; width: 250px; }
  .rent-row { display: flex; gap: 3.5px; margin-bottom: 7px; }
  .rent-row:nth-child(2) { margin-bottom: 4.5px; }
  .rent-row:nth-child(3) { margin-bottom: 5px; }
  .rent-cell { width: 123px; height: 25px; padding: 8px 0 0 14px; font-size: 5px; font-weight: 600; line-height: 1; }
  .rent-row--head .rent-cell { height: 42px; background: var(--cell-head); font-size: 8px; font-weight: 400; padding-top: 9px; }
  .rent-row--body .rent-cell { background: var(--cell-row); }
  .rent-row--accent .rent-cell { background: var(--cell-accent); }

  .folio { position: absolute; left: 25px; bottom: 9.5px; font-size: 6.5px; letter-spacing: 0.1px; }

  .building-photo { position: absolute; right: 0; top: 0; width: 268px; height: 100%; }
</style>
</head>
<body>
  <section class="spread">
    <article class="page page--left">
      <h1 class="page-title">Les plafonds de loyers Beltravigne</h1>
      <p class="body-text intro">Les différentes communes du dispositif Beltravigne appartiennent chacune à une zone. À chaque zone correspond son plafond de loyer. Pour rappel, il s’agit du zonage A / B, le même utilisé pour le calcul des loyers Varennes et le montant des allocations familiales versées par la CNAL. En 2019, les plafonds sont les suivants :</p>

      <div class="rent-table">
        <div class="rent-row rent-row--head">
          <div class="rent-cell">Ut vellabo</div>
          <div class="rent-cell">Ut vellaboNis</div>
        </div>
        <div class="rent-row rent-row--body">
          <div class="rent-cell">Ut vellabo</div>
          <div class="rent-cell">1231421</div>
        </div>
        <div class="rent-row rent-row--body">
          <div class="rent-cell">Ut vellabo</div>
          <div class="rent-cell">12324</div>
        </div>
        <div class="rent-row rent-row--accent">
          <div class="rent-cell">Ut vellabo</div>
          <div class="rent-cell">42312321</div>
        </div>
      </div>

      <p class="body-text note">Il conviendra d’appliquer un coefficient multiplicateur de surface pour le calcul du plafond de loyer applicable.</p>

      <p class="folio">LOI BELTRAVIGNE //6</p>
    </article>

    <article class="page page--right">
      <h2 class="page-title">Principe de la Loi Beltravigne</h2>
      <div class="body-text principle">
        <p>La Loi Beltravigne est entrée en vigueur le 1er janvier 2019. Elle permet de rénover les logements vétustes situés en centres-villes par le biais d’un programme de défiscalisation avantageux à destination des investisseurs. Avec la loi Beltravigne, les contribuables français qui réalisent un investissement immobilier dans l’ancien pourront réduire directement leur impôt d’un pourcentage du prix de revient de l’appartement. Dans le cadre de la loi Beltravigne, les investisseurs doivent s’engager à le louer nu pendant six, neuf ou douze ans à usage de résidence principale.</p>
        <p>La Loi Beltravigne donne droit à 12, 18 ou 21 % de réduction d’impôt du montant investi dans la limite de 300 000 € sur six, neuf ou douze ans. La loi Beltravigne complète le dispositif Varennes.</p>
      </div>

      <svg class="building-photo" role="img" aria-label="Photographie de la résidence rénovée en brique rouge sur fond de ciel bleu, entourée de végétation" viewBox="0 0 268 418" preserveAspectRatio="none">
        <defs>
          <linearGradient id="photo-tones" x1="0" y1="0" x2="0" y2="1">
            <stop offset="0" stop-color="#8fb3d6"/>
            <stop offset="0.25" stop-color="#b9cfe0"/>
            <stop offset="0.45" stop-color="#a4564a"/>
            <stop offset="0.75" stop-color="#8c4a40"/>
            <stop offset="0.88" stop-color="#7a9a5a"/>
            <stop offset="1" stop-color="#9a948e"/>
          </linearGradient>
        </defs>
        <rect width="268" height="418" fill="url(#photo-tones)"/>
      </svg>
    </article>
  </section>
</body>
</html>
```